Nux- luxurious rental suites coming soon

Looking for a large size banner design. The banner will include the logo "NUX". The logo has already been designed by one of your designers (Pelkin). The banner is to be placed on the building fence and will be used as a marketing/ advertisement purpose to display what's coming soon. It needs to be clean and elegant since it's representing upscale apartements.
Requesting Pelkin to be one of the designers. Thanks.

Hi all-here is the logo link. Banner will be printed on 3 separate boards that will be attached side by side to look like one big one. We are doing it this way to be able to make future modifications on 1 board at a time. Each board will be 10'Wx8'H panel. Logo design needs to be in the middle board and other left and right side boards will have the info like "coming soon and building picture". For now, please use any building image, I will be sending the actual building image later on for an update. Please do not include full image of building, choose a section and zoom or crop portion of building image so it looks more interesting. Building will be a luxurious rental in downtown. Thanks. https://www.filvanta.net/sh/k4mrvtq9ws2bdhx/XJR7KW2PL_bn4QLMvhtTcs8Ey?dl=0x

Re: banner: Instead of "coming soon" please use "coming this fall'. Thanks

professionals

Residential rentals

Serif

• use wording such as: coming this fall, 1&2 bedroom suites, designer finishes, terrace views
• Banner will be placed on site over a black mesh backdrop. Please design in a way that will make it look like blending with mesh
• Banner should not be too colorf. Please use white, grey or yellow... refer to logo image

```html
<!DOCTYPE html>
<html lang="en">
<head>
<meta charset="utf-8">
<title>Nux – Luxurious Rental Suites Hoarding</title>
<link rel="stylesheet" href="https://fonts.googleapis.com/css2?family=Open+Sans:wght@400;600;700&display=swap">
<style>
  :root {
    --page: #e9eaec;
    --board-black: #1c1b1d;
    --seam: #3a3a3d;
    --sage-grey: #8d9891;
    --signal-yellow: #f7c600;
    --white: #ffffff;
    --sky-light: #dfe9f3;
    --glass-mid: #4a8fd0;
    --glass-deep: #0d4f97;
  }
  * { margin: 0; padding: 0; box-sizing: border-box; }
  html, body { width: 1200px; height: 815px; overflow: hidden; background: var(--page); }

  .hoarding {
    position: absolute;
    left: 30px; top: 255px;
    width: 1140px; height: 304px;
    display: flex;
  }
  .board {
    position: relative;
    width: 380px; height: 304px;
    overflow: hidden;
    background: var(--board-black);
  }
  .board + .board { border-left: 2px solid var(--seam); }

  .halftone { position: absolute; inset: 0; width: 100%; height: 100%; }

  .teaser {
    position: absolute;
    left: 78px; bottom: 22px;
    transform-origin: left bottom;
    transform: rotate(-58deg);
    font-family: "Open Sans", sans-serif;
    font-weight: 600;
    font-size: 30px;
    color: var(--sage-grey);
    white-space: nowrap;
  }

  .brand {
    position: absolute;
    left: 50%; top: 50%;
    transform: translate(-50%, -50%);
    text-align: center;
    white-space: nowrap;
    font-family: "Open Sans", sans-serif;
    font-weight: 600;
    color: var(--sage-grey);
  }
  .brand-name {
    font-size: 92px;
    line-height: 1;
    letter-spacing: 6px;
  }
  .brand-address {
    margin-top: 10px;
    font-size: 16px;
    letter-spacing: 3px;
  }

  .building-photo {
    position: absolute; inset: 0;
    background:
      linear-gradient(128deg, var(--sky-light) 0%, var(--sky-light) 26%, transparent 27%),
      linear-gradient(150deg, var(--glass-mid) 0%, var(--glass-deep) 100%);
  }
  .features {
    position: absolute;
    left: 150px; bottom: 14px;
    transform-origin: left bottom;
    transform: rotate(-57deg);
    font-family: "Open Sans", sans-serif;
    white-space: nowrap;
  }
  .features-headline {
    font-weight: 700;
    font-size: 36px;
    line-height: 1.05;
    color: var(--signal-yellow);
    text-transform: uppercase;
  }
  .features-list {
    margin-top: 6px;
    font-weight: 600;
    font-size: 27px;
    line-height: 1.15;
    color: var(--white);
    list-style: none;
  }
</style>
</head>
<body>
  <main class="hoarding">
    <section class="board board-teaser">
      <svg class="halftone" viewBox="0 0 380 304" role="img" aria-label="Yellow halftone dot pattern fading toward the corner">
        <defs>
          <linearGradient id="teaserDots" x1="1" y1="1" x2="0.4" y2="0.5">
            <stop offset="0" stop-color="#f7c600" stop-opacity="0.85"/>
            <stop offset="1" stop-color="#f7c600" stop-opacity="0.1"/>
          </linearGradient>
        </defs>
        <polygon points="175,304 380,304 380,118" fill="url(#teaserDots)"/>
      </svg>
      <p class="teaser">...coming this fall</p>
    </section>

    <section class="board board-brand">
      <svg class="halftone" viewBox="0 0 380 304" role="img" aria-label="Yellow halftone dot patterns in the lower left and upper right corners">
        <defs>
          <linearGradient id="brandDotsLow" x1="0" y1="1" x2="0.6" y2="0">
            <stop offset="0" stop-color="#f7c600" stop-opacity="0.85"/>
            <stop offset="1" stop-color="#f7c600" stop-opacity="0.1"/>
          </linearGradient>
          <linearGradient id="brandDotsHigh" x1="1" y1="0" x2="0.4" y2="0.6">
            <stop offset="0" stop-color="#f7c600" stop-opacity="0.85"/>
            <stop offset="1" stop-color="#f7c600" stop-opacity="0.1"/>
          </linearGradient>
        </defs>
        <polygon points="0,304 0,118 58,304" fill="url(#brandDotsLow)"/>
        <polygon points="296,0 380,0 380,190" fill="url(#brandDotsHigh)"/>
      </svg>
      <div class="brand">
        <p class="brand-name">NUX</p>
        <p class="brand-address">415 MARLOWE</p>
      </div>
    </section>

    <section class="board board-features">
      <div class="building-photo" role="img" aria-label="Close-up of a blue glass tower facade reflecting sky, with a perforated white panel in the upper left corner"></div>
      <div class="features">
        <h2 class="features-headline">Luxurious<br>Rental Suites</h2>
        <ul class="features-list">
          <li>1&amp;2 bedroom suites</li>
          <li>designer finishes</li>
        </ul>
      </div>
    </section>
  </main>
</body>
</html>
```